Corrow Family Farm fresh honey jar label

I need a label for jars of honey harvested at our farm. These are for gifts and personal use. We are looking to incorporate our farm brand into the label. We would like the design to take the existing brand and add some element like bees, honey, flowers, or hives to indicate the contents. We want the design to feel homemade and authentic without feeling cheap or hoaky

Requirements
Must have
• The label must be made to fit a 1" x2" rectangular label. The label must include the attached family brand. The label must include the text "Corrow Family Farms" "Pinebrook, USA" "Farm Fresh Honey". The label will be printed on off-white paper
Nice to have
• It would be nice to have illustrations of bees or flowers around the logo or hives or honeycombs. The label should have a vintage feel
Should not have
• The label should not feel overly cartoonish or hoaky

```html
<!DOCTYPE html>
<html lang="en">
<head>
<meta charset="utf-8">
<title>Corrow Family Farms – Farm Fresh Honey Label</title>
<link rel="stylesheet" href="https://fonts.googleapis.com/css2?family=Tinos:wght@400;700&display=swap">
<style>
  :root {
    --backdrop: #b8b8b8;
    --paper: #efe9df;
    --ink-brown: #4a3816;
    --accent-copper: #c0692e;
    --ribbon-text: #fbf4ea;
    --bloom-peach: #f6cf92;
    --bloom-gold: #e9b45e;
    --leaf-green: #2f5e4e;
  }
  * { margin: 0; padding: 0; box-sizing: border-box; }
  html, body {
    width: 1200px;
    height: 675px;
    overflow: hidden;
    background: var(--backdrop);
  }
  .stage {
    width: 1200px;
    height: 675px;
    display: flex;
    align-items: center;
    justify-content: center;
  }
  .honey-label {
    width: 900px;
    height: 454px;
    display: block;
    overflow: visible;
    filter: drop-shadow(6px 8px 6px rgba(0, 0, 0, 0.22));
    font-family: "Tinos", "Times New Roman", serif;
  }
  .label-paper { fill: var(--paper); }
  .frame-outer { fill: none; stroke: var(--ink-brown); stroke-width: 2.5; }
  .frame-inner { fill: none; stroke: var(--accent-copper); stroke-width: 2.5; }
  .ribbon-band { fill: none; stroke: var(--accent-copper); stroke-width: 36; }
  .ribbon-dot { fill: var(--accent-copper); }
  .ribbon-text {
    fill: var(--ribbon-text);
    font-size: 21px;
    font-weight: 700;
    letter-spacing: 5px;
  }
  .brand-mark {
    fill: var(--ink-brown);
    font-size: 30px;
    letter-spacing: 4px;
  }
  .farm-name {
    fill: var(--ink-brown);
    font-size: 62px;
  }
  .name-dot { fill: var(--ink-brown); }
  .detail-text {
    fill: var(--ink-brown);
    font-size: 15px;
    letter-spacing: 2px;
  }
</style>
</head>
<body>
<main class="stage">
  <svg class="honey-label" viewBox="0 0 900 454" xmlns="http://www.w3.org/2000/svg" aria-label="Corrow Family Farms farm fresh honey label">
    <defs>
      <path id="label-outline" d="M30 59 L240 59 C330 -20 570 -20 660 59 L870 59 A30 30 0 0 0 900 89 L900 365 A30 30 0 0 0 870 395 L660 395 C570 474 330 474 240 395 L30 395 A30 30 0 0 0 0 365 L0 89 A30 30 0 0 0 30 59 Z"/>
      <path id="ribbon-curve" d="M292 128 Q450 40 608 128"/>
      <clipPath id="inner-area">
        <use href="#label-outline" transform="translate(37 33) scale(0.918 0.855)"/>
      </clipPath>
      <linearGradient id="bloom-fill" x1="0" y1="0" x2="0" y2="1">
        <stop offset="0" stop-color="var(--bloom-peach)"/>
        <stop offset="0.5" stop-color="var(--bloom-gold)"/>
        <stop offset="1" stop-color="var(--leaf-green)"/>
      </linearGradient>
    </defs>

    <use href="#label-outline" class="label-paper"/>

    <path class="bloom-illustration" role="img" aria-label="Illustration of a honeybee among peach blossoms and dark green leaves"
          fill="url(#bloom-fill)" clip-path="url(#inner-area)"
          d="M265 335 Q290 285 350 288 Q390 266 420 274 Q452 240 492 266 Q540 266 560 290 Q620 290 640 335 L640 470 L265 470 Z"/>

    <use href="#label-outline" class="frame-outer" transform="translate(16 14) scale(0.9644 0.938)"/>
    <use href="#label-outline" class="frame-inner" transform="translate(34 30) scale(0.9244 0.868)"/>

    <g class="ribbon">
      <use href="#ribbon-curve" class="ribbon-band"/>
      <circle class="ribbon-dot" cx="272" cy="138" r="6"/>
      <circle class="ribbon-dot" cx="628" cy="138" r="6"/>
      <text class="ribbon-text" text-anchor="middle">
        <textPath href="#ribbon-curve" startOffset="50%" dy="7">FARM FRESH HONEY</textPath>
      </text>
    </g>

    <text class="brand-mark" x="450" y="178" text-anchor="middle">CORROW</text>

    <circle class="name-dot" cx="48" cy="228" r="7"/>
    <text class="farm-name" x="450" y="250" text-anchor="middle" textLength="760" lengthAdjust="spacingAndGlyphs">CORROW FAMILY FARMS</text>
    <circle class="name-dot" cx="852" cy="228" r="7"/>

    <text class="detail-text" x="95" y="285">PINEBROOK, USA</text>
    <text class="detail-text" x="805" y="285" text-anchor="end">NET WT. 100G</text>
  </svg>
</main>
</body>
</html>
```